Business Card Design Project

Use our current logo. Clean design.

Industry/Entity Type

Business

Requirements
Must have
• Marisela DUBRANCQ
M. Law
Managing Partner

Alpenvorsa AG
Kornhalmweg 214
CH-3097 Liebefeld

M. +41 79 412 56 27
T. +41 31 928 44 10
F. +41 31 928 44 19

m.dubrancq@alpenvorsa-example.com
www.alpenvorsa-example.com

```html
<!DOCTYPE html>
<html lang="en">
<head>
<meta charset="utf-8">
<title>Alpenvorsa AG – Business Card</title>
<link href="https://fonts.googleapis.com/css2?family=Mulish:ital,wght@0,400;0,600;0,700;1,400&display=swap" rel="stylesheet">
<style>
  :root {
    --backdrop: #0e0e0e;
    --card-top: #f6f6f6;
    --card-bottom: #e9e9e9;
    --band: #2a2726;
    --ink: #1d1b1b;
    --ink-soft: #333;
  }
  * { margin: 0; padding: 0; box-sizing: border-box; }
  html, body { width: 1200px; height: 900px; overflow: hidden; }
  body {
    background: var(--backdrop);
    font-family: "Mulish", "Helvetica Neue", Arial, sans-serif;
    color: var(--ink);
    position: relative;
  }
  .card {
    position: absolute;
    left: 370px;
    width: 449px;
    height: 268px;
    background: linear-gradient(180deg, var(--card-top), var(--card-bottom));
    overflow: hidden;
  }
  .card--front { top: 133px; }
  .card--back { top: 452px; background: linear-gradient(180deg, #fafafa, #f0f0f0); }
  .band {
    position: absolute;
    top: 0;
    bottom: 0;
    background: var(--band);
  }
  .card--front .band { left: 0; width: 20px; }
  .card--back .band { right: 0; width: 30px; }

  .brand {
    position: absolute;
    font-weight: 600;
    letter-spacing: 0.02em;
    color: var(--ink);
    white-space: nowrap;
  }
  .card--front .brand { left: 48px; top: 96px; font-size: 15px; }
  .card--back .brand { right: 52px; top: 148px; font-size: 20px; }

  .person { position: absolute; left: 48px; top: 142px; font-size: 11px; line-height: 13px; }
  .person__name { font-weight: 700; }
  .person__role { font-style: italic; }

  .contact { position: absolute; left: 48px; top: 193px; font-size: 9px; line-height: 12px; color: var(--ink-soft); }
  .contact__row { display: flex; }
  .contact__label { width: 53px; }

  .web {
    position: absolute;
    right: 73px;
    top: 172px;
    font-size: 9px;
    color: var(--ink-soft);
  }
  .rule {
    position: absolute;
    left: 39px;
    right: 30px;
    top: 197px;
    height: 3px;
    background: var(--ink);
  }
  .address {
    position: absolute;
    right: 36px;
    top: 204px;
    font-size: 9px;
    color: var(--ink-soft);
  }
</style>
</head>
<body>
  <section class="card card--front">
    <div class="band"></div>
    <div class="brand">ALPENVORSA</div>
    <div class="person">
      <div class="person__name">Marisela DUBRANCQ</div>
      <div>M. Law</div>
      <div class="person__role">Managing Partner</div>
    </div>
    <div class="contact">
      <div>m.dubrancq@alpenvorsa-example.com</div>
      <div class="contact__row"><span class="contact__label">Mobile:</span><span>+41 79 412 56 27</span></div>
      <div class="contact__row"><span class="contact__label">Telephone:</span><span>+41 31 928 44 10</span></div>
      <div class="contact__row"><span class="contact__label">Facsimile:</span><span>+41 31 928 44 19</span></div>
    </div>
  </section>

  <section class="card card--back">
    <div class="band"></div>
    <div class="brand">ALPENVORSA</div>
    <div class="web">www.alpenvorsa-example.com</div>
    <div class="rule"></div>
    <div class="address">Alpenvorsa AG, Kornhalmweg 214, CH-3097 Liebefeld</div>
  </section>
</body>
</html>
```